Education Certificate

We need a modern yet professional Certificate for those who successfully pass / complete our online Training course.

There are various courses but ONE certificate design required.

the certificate needs to look extremely professional and of value.

```html
<!DOCTYPE html>
<html lang="en">
<head>
<meta charset="utf-8">
<title>Certificate of Completion</title>
<link href="https://fonts.googleapis.com/css2?family=Playfair+Display:wght@900&family=Poppins:wght@500&family=Montserrat:wght@500;600&family=Mrs+Saint+Delafield&display=swap" rel="stylesheet">
<style>
  :root{
    --navy-deep:#0d1a4f;
    --navy:#27306f;
    --blue:#3341ae;
    --blue-dark:#1f2a80;
    --gold:#e6c944;
    --gold-soft:#e9d77a;
    --ink:#111111;
    --paper:#ffffff;
    --paper-shade:#f3f3f5;
  }
  *{margin:0;padding:0;box-sizing:border-box}
  html,body{width:1200px;height:880px;overflow:hidden}
  body{background:var(--paper)}
  .certificate{
    position:relative;width:1200px;height:880px;overflow:hidden;
    background:radial-gradient(ellipse at 50% 55%, var(--paper) 0%, var(--paper) 45%, var(--paper-shade) 100%);
  }
  .corners,.seal{position:absolute;left:0;top:0}
  .issuer{
    position:absolute;left:0;right:0;top:62px;
    display:flex;justify-content:center;align-items:center;gap:14px;
  }
  .issuer-mark{width:26px;height:26px;background:var(--navy)}
  .issuer-name{
    font-family:"Montserrat",sans-serif;font-weight:600;font-size:21px;
    letter-spacing:.06em;text-transform:uppercase;color:var(--navy);
  }
  .title{
    position:absolute;left:0;right:0;top:178px;text-align:center;
    font-family:"Playfair Display",serif;font-weight:900;font-size:94px;
    line-height:1;letter-spacing:.02em;
    color:var(--blue);
    background:linear-gradient(180deg,var(--blue) 0%,var(--blue-dark) 100%);
    -webkit-background-clip:text;background-clip:text;-webkit-text-fill-color:transparent;
  }
  .subtitle{
    position:absolute;left:283px;width:632px;top:272px;
    display:flex;align-items:center;gap:14px;
    font-family:"Playfair Display",serif;font-weight:900;font-size:31px;
    letter-spacing:.04em;color:var(--ink);white-space:nowrap;
  }
  .subtitle::before,.subtitle::after{content:"";flex:1;height:1.5px;background:var(--gold-soft)}
  .presented{
    position:absolute;left:0;right:0;top:370px;text-align:center;
    font-family:"Poppins",sans-serif;font-weight:500;font-size:25px;
    letter-spacing:.31em;color:var(--ink);
  }
  .recipient{
    position:absolute;left:222px;width:715px;top:418px;height:102px;
    border-bottom:1.5px solid var(--navy);
    text-align:center;
    font-family:"Mrs Saint Delafield",cursive;font-size:100px;line-height:110px;
    color:var(--blue-dark);
  }
  .field{
    position:absolute;left:222px;width:715px;display:flex;align-items:flex-end;gap:18px;
    font-family:"Montserrat",sans-serif;font-weight:500;font-size:23px;color:var(--ink);
  }
  .field::after{content:"";flex:1;height:1.5px;background:var(--navy);margin-bottom:6px}
  .field-course{top:552px}
  .field-duration{top:614px}
  .sign-block{
    position:absolute;top:766px;width:285px;border-top:1.5px solid var(--navy);
    padding-top:8px;text-align:center;
    font-family:"Montserrat",sans-serif;font-weight:500;font-size:23px;color:var(--ink);
  }
  .sign-date{left:224px}
  .sign-signature{left:657px}
</style>
</head>
<body>
<main class="certificate">
  <svg class="corners" width="1200" height="880" viewBox="0 0 1200 880" aria-hidden="true">
    <g class="corner-top-left">
      <polygon points="0,0 200,0 0,386" fill="var(--navy)"/>
      <polygon points="0,0 120,0 0,230" fill="var(--navy-deep)"/>
      <polygon points="48,167 93,167 16,386 0,386 0,300" fill="var(--gold)"/>
      <polygon points="93,167 108,167 18,400 16,386" fill="var(--paper)"/>
      <line x1="108" y1="198" x2="17" y2="405" stroke="var(--navy)" stroke-width="2.5"/>
    </g>
    <g class="corner-bottom-right" transform="rotate(180 600 440)">
      <polygon points="0,0 200,0 0,386" fill="var(--navy)"/>
      <polygon points="0,0 120,0 0,230" fill="var(--navy-deep)"/>
      <polygon points="48,167 93,167 16,386 0,386 0,300" fill="var(--gold)"/>
      <polygon points="93,167 108,167 18,400 16,386" fill="var(--paper)"/>
      <line x1="108" y1="198" x2="17" y2="405" stroke="var(--navy)" stroke-width="2.5"/>
    </g>
  </svg>

  <svg class="seal" width="1200" height="880" viewBox="0 0 1200 880" role="img" aria-label="Award seal">
    <defs>
      <radialGradient id="seal-gold" cx="45%" cy="40%" r="65%">
        <stop offset="0%" stop-color="#fbf3c4"/>
        <stop offset="55%" stop-color="#e0be55"/>
        <stop offset="100%" stop-color="#a57d1f"/>
      </radialGradient>
    </defs>
    <polygon points="1032,150 1014,220 1036,210 1050,232 1070,160" fill="var(--blue-dark)"/>
    <polygon points="1080,160 1098,232 1112,212 1134,220 1110,150" fill="var(--blue-dark)"/>
    <circle cx="1066" cy="105" r="78" fill="var(--blue)"/>
    <circle cx="1066" cy="105" r="64" fill="url(#seal-gold)"/>
    <circle cx="1066" cy="105" r="52" fill="#f4efe0"/>
  </svg>

  <header class="issuer">
    <span class="issuer-mark" aria-hidden="true"></span>
    <span class="issuer-name">Meridian Service Learning Academy</span>
  </header>

  <h1 class="title">CERTIFICATE</h1>
  <p class="subtitle">OF COMPLETION</p>

  <p class="presented">THIS CERTIFICATE IS PROUDLY PRESENTED TO</p>
  <p class="recipient">Jordan Ashcroft</p>

  <p class="field field-course">COURSE NAME</p>
  <p class="field field-duration">DURATION</p>

  <p class="sign-block sign-date">DATE</p>
  <p class="sign-block sign-signature">SIGNATURE</p>
</main>
</body>
</html>
```